Ledgerwise Reach - B2B Demand Generation Website Project

We need a fully functional website for www.ledgerwisereach.example. We are a B2B Demand Generation company, based in London, working with companies such as QRT, VKD, Norvex, Brindlow, Tarvo generating them sales leads for their sales teams. We run this through digital marketing newsletter promotions and have a network of websites. Content syndication, data, demand generation, online marketing. Our logo has just been redone (attached) and we have a holding page already which i would like to use the style / colours. Our logo is bright and vibrant but i dont want the site to be a rainbow. We are expensive, classy, professorial, B2B, intelligent.

Home
About Us
Our Services
Prospora & QA Technology
Intent Data
Testimonials
Contact Us
Updates

Target Market(s)

B2B Marketers (QRT, Velquarion, Tarvo, VKD, Opal Reach, Driftmoor, Harlow Quantis, Technology Companies, Data Companies, Marketing Teams, Tumbleden.

Industry/Entity Type

Marketing

Coding

Coded - Design and coding required

Number of Pages Required

5+ page

Font styles to use
Sans Serif

Requirements
Must have
• Home
About Us
Our Services
Prospora & QA Technology
Intent Data
Testimonials
Contact Us

Simple Pages.

Look classy, intelligent, data experts. I like the video homepages were the image moves at the top. Very soft animation.
Nice to have
• Websites i like:

https://www.vkd.example/
https://www.brevantor.example/
https://www.plumfieldsites.example.co.uk/

Ledgerwise Reach - The Demand Generation Company
Should not have
• Glimpsevault crap images

```html
<!DOCTYPE html>
<html lang="en">
<head>
<meta charset="utf-8">
<title>Ledgerwise Reach - The Demand Generation Company</title>
<link rel="stylesheet" href="https://fonts.googleapis.com/css2?family=Poppins:ital,wght@0,300;0,400;0,500;0,600;1,400&display=swap">
<style>
:root{
  --blue:#1d5fa6;
  --blue-dark:#1a5a9c;
  --sky:#5aa9ec;
  --sky-light:#8cc6f5;
  --red:#b3201f;
  --ink:#1b1b1b;
  --text:#333;
  --muted:#777;
  --icon-bg:#d9ecfb;
  --pink-wash:#fbf0f6;
  --mint-wash:#eefbfb;
  --line:#e4e4e4;
}
*{box-sizing:border-box;margin:0;padding:0}
html,body{width:1200px;height:3659px;overflow:hidden}
body{position:relative;background:#fff;font-family:'Poppins',sans-serif;color:var(--text)}
.abs{position:absolute}
.btn{display:flex;align-items:center;justify-content:center;background:var(--red);color:#fff;font-size:10px;font-weight:600;letter-spacing:.3px;text-transform:uppercase}

/* decorative washes */
.washes{left:0;top:0;width:1200px;height:3659px}

/* header */
.brand{display:flex;align-items:center;gap:12px}
.brand-dot{width:52px;height:52px;border-radius:50%;background:var(--red);opacity:.85}
.brand-name{font-size:30px;font-weight:400;color:var(--blue);line-height:1;letter-spacing:-.5px}
.brand-tag{font-size:8px;color:var(--blue);margin-top:3px}
.head-contact{display:flex;align-items:center;gap:14px}
.head-icon{width:40px;height:40px;border-radius:50%;background:#e8f1fa;display:flex;align-items:center;justify-content:center}
.head-label{font-size:9px;font-weight:600;color:var(--ink)}
.head-value{font-size:10px;color:var(--ink)}
.nav{left:234px;top:94px;width:732px;height:48px;background:var(--blue-dark);display:flex;align-items:center;padding:0 20px;gap:30px;z-index:3}
.nav a{color:#fff;font-size:9.5px;font-weight:500;text-decoration:none;text-transform:uppercase;display:flex;align-items:center;gap:8px}
.nav-ring{width:16px;height:16px;border-radius:50%;border:3px solid #9cc9f0;background:var(--blue)}

/* hero */
.hero{left:0;top:119px;width:1200px;height:540px}
.hero-title{left:0;top:258px;width:1200px;text-align:center;color:#fff;font-size:64px;font-weight:400;letter-spacing:1px}
.hero-sub{left:0;top:333px;width:1200px;text-align:center;color:#fff;font-size:20px;font-weight:300;letter-spacing:.5px}
.hero-btn{left:528px;top:383px;width:145px;height:39px;border:2px solid #fff;color:#fff;font-size:10px;display:flex;align-items:center;justify-content:center;letter-spacing:.5px}

/* welcome */
.welcome-kicker{left:234px;top:711px;font-size:12px;font-weight:500;color:var(--ink)}
.welcome-name{left:234px;top:722px;font-size:33px;color:var(--red);font-weight:400}
.welcome-copy{left:234px;top:772px;width:305px;font-size:10px;line-height:16.3px;color:var(--ink)}
.divider{left:552px;top:716px;width:1px;height:218px;background:var(--red)}
.work-title{left:577px;top:708px;font-size:17px;font-weight:500;color:var(--ink)}
.work-list{left:581px;top:737px;font-size:9.5px;color:var(--ink)}
.stat{width:125px;height:118px;background:#fff;box-shadow:0 2px 10px rgba(0,0,0,.07);text-align:center;top:771px}
.stat-kicker{font-size:8px;color:var(--blue);margin-top:26px}
.stat-num{font-size:23px;color:var(--ink);margin-top:2px}
.stat-label{font-size:7.5px;font-weight:500;color:var(--ink);line-height:13px;margin-top:2px}
.learn-btn{left:490px;top:933px;width:125px;height:41px}

/* services */
.section-title{font-size:33px;font-weight:400}
.t-red{color:var(--red)}
.t-blue{color:var(--blue)}
.services-title{left:234px;top:1275px}
.services-copy{left:234px;top:1325px;width:210px;font-size:10px;line-height:14.5px;color:var(--ink)}
.explore-btn{left:234px;top:1434px;width:125px;height:41px}
.card{background:#fff;box-shadow:0 2px 14px rgba(0,0,0,.06);text-align:center;padding:26px 20px 0}
.svc-icon{width:78px;height:78px;border-radius:50%;background:var(--icon-bg);margin:0 auto;display:flex;align-items:center;justify-content:center}
.svc-title{font-size:12px;font-weight:500;color:var(--ink);line-height:19px;margin-top:16px;text-transform:uppercase}
.svc-copy{font-size:11px;color:var(--ink);line-height:19px;margin-top:12px}

/* testimonials */
.testi-title{left:0;top:1728px;width:1200px;text-align:center;color:var(--blue)}
.quote-mark{left:0;top:1854px;width:1200px;text-align:center;font-family:Georgia,serif;font-size:110px;color:var(--red);font-weight:700;line-height:1}
.quote-text{left:330px;top:1926px;width:540px;text-align:center;font-style:italic;font-size:14.5px;line-height:21.4px;color:#555}
.avatar{left:568px;top:2075px;width:64px;height:64px;border-radius:50%;background:radial-gradient(circle at 50% 40%,#e9c9b4,#7a4a35)}
.testi-name{left:0;top:2157px;width:1200px;text-align:center;font-size:12px;color:#555}
.testi-role{left:0;top:2175px;width:1200px;text-align:center;font-size:8px;color:var(--red)}
.dots{left:572px;top:2227px;display:flex;gap:14px}
.dots span{width:5px;height:5px;border-radius:50%;background:#f0b8c4}
.dots span:first-child{background:var(--red)}

/* news */
.news-title{left:0;top:2385px;width:1200px;text-align:center}
.news-card{top:2454px;width:232px;height:233px;background:#fff;box-shadow:0 3px 12px rgba(0,0,0,.09);padding:24px 24px 0}
.news-head{font-size:12.5px;font-weight:500;color:var(--ink);line-height:19px}
.news-meta{font-size:9.5px;color:var(--muted);margin-top:9px}
.news-copy{font-size:9.5px;color:#555;line-height:17.5px;margin-top:10px}
.read-more{display:flex;align-items:center;gap:12px;font-size:11px;color:var(--ink);margin-top:14px}
.read-more i{width:24px;height:24px;border-radius:50%;border:3px solid #f2c2c2;background:#fff}

/* contact */
.contact-art{left:206px;top:2780px;width:270px;height:390px;border-radius:40% 50% 30% 40%;background:linear-gradient(160deg,#9a58d8 0%,#35b8c0 55%,#e7f3fb 100%);opacity:.85}
.contact-title{left:578px;top:2826px;font-size:23px;font-weight:500;color:var(--ink);line-height:29px}
.contact-copy{left:580px;top:2888px;width:390px;font-size:10px;line-height:15.5px;color:var(--ink)}
.field{border:1px solid var(--line);background:#fff;font-size:9.5px;color:#777;padding:12px 14px 0}
.submit-btn{left:578px;top:3127px;width:125px;height:41px}

/* footer */
.footer-bg{left:0;top:3278px;width:1200px;height:381px;background:linear-gradient(180deg,#fdf3f7 0%,#fbeef3 100%)}
.foot-brand{left:234px;top:3345px;width:250px;text-align:center}
.foot-brand .brand-dot{width:48px;height:48px;margin:0 auto 6px}
.foot-name{font-size:24px;color:var(--red)}
.foot-tag{font-size:7px;color:var(--blue)}
.foot-copy{left:234px;top:3448px;width:250px;text-align:center;font-size:9px;line-height:15px;color:var(--ink)}
.foot-col h4{font-size:10.5px;font-weight:600;color:var(--ink);margin-bottom:14px}
.foot-col li{list-style:none;font-size:9px;color:var(--ink);line-height:17.6px}
.foot-contact li{display:flex;gap:10px;align-items:flex-start;margin-bottom:6px;line-height:15px}
.copyright{left:234px;top:3612px;font-size:8.5px;color:var(--ink)}
.social{left:918px;top:3610px;display:flex;gap:22px}
.social span{width:13px;height:13px;border-radius:50%;background:#1a3d6a}
</style>
</head>
<body>

<svg class="abs washes" viewBox="0 0 1200 3659" aria-hidden="true">
  <path d="M0 610 C180 560 380 640 560 760 C700 860 760 960 720 1050 C600 1040 200 1030 0 1020Z" fill="#f7f0fa"/>
  <path d="M840 1000 C980 960 1160 980 1200 1060 L1200 1630 C1040 1650 860 1600 800 1500 C760 1380 820 1260 780 1160 C760 1090 790 1030 840 1000Z" fill="#eefbfd"/>
  <path d="M260 1760 C380 1700 560 1720 700 1760 C880 1810 960 1900 920 2040 C880 2160 820 2280 640 2320 C520 2350 460 2230 380 2150 C280 2040 180 1880 260 1760Z" fill="#fcf1f7"/>
  <path d="M0 2750 C200 2700 420 2760 560 2850 L560 3260 L0 3260Z" fill="#fdf6f9"/>
</svg>

<!-- header -->
<div class="abs brand" style="left:234px;top:17px">
  <div class="brand-dot"></div>
  <div><div class="brand-name">ledgerwise reach</div><div class="brand-tag">The Demand Generation Company</div></div>
</div>
<div class="abs head-contact" style="left:625px;top:26px">
  <div class="head-icon"><svg width="16" height="12" viewBox="0 0 16 12"><rect width="16" height="12" rx="1.5" fill="var(--blue)"/><path d="M1 1l7 5 7-5" stroke="#fff" stroke-width="1.4" fill="none"/></svg></div>
  <div><div class="head-label">EMAIL US</div><div class="head-value">info@ledgerwisereach.example</div></div>
</div>
<div class="abs head-contact" style="left:831px;top:26px">
  <div class="head-icon"><svg width="16" height="16" viewBox="0 0 24 24"><path fill="var(--blue)" d="M6.6 10.8a15 15 0 006.6 6.6l2.2-2.2a1 1 0 011-.25 11.4 11.4 0 003.6.6 1 1 0 011 1V20a1 1 0 01-1 1A17 17 0 013 4a1 1 0 011-1h3.5a1 1 0 011 1c0 1.25.2 2.45.57 3.57a1 1 0 01-.25 1z"/></svg></div>
  <div><div class="head-label">CALL US</div><div class="head-value">+44 20 7946 0182</div></div>
</div>

<nav class="abs nav">
  <a href="#"><span class="nav-ring"></span>Home</a>
  <a href="#">About Us</a>
  <a href="#">Our Services</a>
  <a href="#">Prospora &amp; QA Technology</a>
  <a href="#">Intent Data</a>
  <a href="#">Testimonials</a>
  <a href="#">Contact Us</a>
</nav>

<!-- hero -->
<svg class="abs hero" viewBox="0 0 1200 540" preserveAspectRatio="none" aria-hidden="true">
  <defs><linearGradient id="heroGrad" x1="0" y1="0" x2="1" y2="1"><stop offset="0" stop-color="#7dbdf2"/><stop offset=".55" stop-color="#5aa6ea"/><stop offset="1" stop-color="#3f8fe0"/></linearGradient></defs>
  <path d="M0 0H1200V470C1120 520 1000 540 880 500C760 455 640 380 500 400C360 420 250 470 140 450C70 438 30 430 0 440Z" fill="url(#heroGrad)"/>
  <path d="M0 440C60 420 140 400 240 420C360 445 440 430 540 400C660 360 760 430 880 480C1000 530 1120 500 1200 460" stroke="#a9d4f7" stroke-width="1" fill="none" opacity=".6"/>
</svg>
<h1 class="abs hero-title">ledgerwise reach</h1>
<div class="abs hero-sub">The Demand&nbsp; Generation Company</div>
<a class="abs hero-btn">CONTACT US</a>

<!-- welcome -->
<div class="abs welcome-kicker">WELCOME TO</div>
<div class="abs welcome-name">ledgerwise reach</div>
<p class="abs welcome-copy">Ledgerwise Reach offers multi-channel demand generation services to publishers and technology vendors through our network of lead generation websites and native speaking telemarketing agents. Whether looking for MQL, ABM or BANT campaigns, Ledgerwise Reach can assist you in delivering your demand generation strategy and generate pipeline for your sales teams and/or channel partners.</p>
<div class="abs divider"></div>
<h2 class="abs work-title">WHO WE WORK WITH</h2>
<div class="abs work-list">QRT, Tarvo, VKD, Corvane, Skyledger, Oriquest, Weekline, Cintrel, Markessa</div>
<div class="abs stat" style="left:575px"><div class="stat-kicker">Ticker to</div><div class="stat-num">70,000+</div><div class="stat-label">Downloads Per<br>Month</div></div>
<div class="abs stat" style="left:707px"><div class="stat-kicker">Ticker to</div><div class="stat-num">25,000+</div><div class="stat-label">Leads Delivered<br>Per Month</div></div>
<div class="abs stat" style="left:841px"><div class="stat-kicker">Ticker to</div><div class="stat-num">50+</div><div class="stat-label">Countries We Can<br>Reach</div></div>
<a class="abs btn learn-btn">Learn More</a>

<!-- services -->
<h2 class="abs section-title services-title"><span class="t-red">our</span> <span class="t-blue">services</span></h2>
<p class="abs services-copy">Lorem ipsum dolor sit amet, consectetur adipiscing elit. Pellentesque non cursus risus. Pellentesque vel blandit diam. Ut imperdiet iaculis nibh vitae dictum. Aenean dapibus eros sed ligula vehicula ullamcorper.</p>
<a class="abs btn explore-btn">Explore More</a>

<div class="abs card" style="left:484px;top:1079px;width:232px;height:267px">
  <div class="svc-icon"><svg width="40" height="34" viewBox="0 0 40 34" fill="none" stroke="var(--blue)" stroke-width="1.6"><circle cx="20" cy="10" r="4"/><circle cx="9" cy="15" r="3"/><circle cx="31" cy="15" r="3"/><path d="M12 30c0-5 4-9 8-9s8 4 8 9M3 30c0-4 3-7 6-7M37 30c0-4-3-7-6-7"/><path d="M20 1v2M13 4l1.5 1.5M27 4l-1.5 1.5"/></svg></div>
  <div class="svc-title">Marketing Qualified Leads<br>(MQL)</div>
  <p class="svc-copy">A Marketing Qualified Lead (MQL) is a prospect that has expressed an interest in what your brand has to offer.</p>
</div>
<div class="abs card" style="left:484px;top:1367px;width:232px;height:269px">
  <div class="svc-icon"><svg width="34" height="38" viewBox="0 0 34 38" fill="none" stroke="var(--blue)" stroke-width="1.6"><rect x="3" y="5" width="24" height="30" rx="2"/><rect x="10" y="2" width="10" height="5" rx="1"/><circle cx="11" cy="24" r="4"/><rect x="17" y="19" width="14" height="16" rx="1"/><path d="M20 23h8M20 27h8M20 31h8M8 12h14"/></svg></div>
  <div class="svc-title">Account Based Marketing<br>Leads (ABM)</div>
  <p class="svc-copy">ABM is a strategy that directs marketing resources to engaging a specific set of target accounts.</p>
</div>
<div class="abs card" style="left:734px;top:1235px;width:232px;height:267px">
  <div class="svc-icon"><svg width="42" height="36" viewBox="0 0 42 36" fill="none" stroke="var(--blue)" stroke-width="1.6"><circle cx="8" cy="8" r="5"/><path d="M8 5v6M6 7h4"/><path d="M4 34V26M10 34V22M16 34V24M22 34V18M28 34V14M34 34V10"/><path d="M14 18L24 10l5 4 9-9M33 5h5v5"/></svg></div>
  <div class="svc-title">Sales Qualified Lead<br>/ BANT</div>
  <p class="svc-copy">An SQL lead or a BANT lead is a type of lead that expressed a specific interest in a product and service that you have to offer...</p>
</div>

<!-- testimonials -->
<h2 class="abs section-title testi-title">testimonials</h2>
<div class="abs quote-mark">&ldquo;</div>
<p class="abs quote-text">Lorem ipsum dolor sit amet, consectetur adipiscing elit. Pellentesque non cursus risus. Pellentesque vel blandit diam. Ut imperdiet iaculis nibh vitae dictum. Aenean dapibus eros sed ligula vehicula ullamcorper. Curabitur aliquet consequat ex ac eleifend. Donec nec arcu est. Pellentesque scelerisque rutrum est, in ultrices enim pharetra quis.</p>
<div class="abs avatar" role="img" aria-label="Portrait photo of the client giving the testimonial"></div>
<div class="abs testi-name">ROSALIND PEMBERTON</div>
<div class="abs testi-role">SALES MANAGER</div>
<div class="abs dots"><span></span><span></span><span></span><span></span></div>

<!-- news -->
<h2 class="abs section-title news-title"><span class="t-red">latest</span> <span class="t-blue">news</span></h2>
<article class="abs news-card" style="left:234px">
  <h3 class="news-head">Lorem ipsum dolor sit amet, consectetur adipiscing elit.</h3>
  <div class="news-meta">by Tobias Greene, on June 22</div>
  <p class="news-copy">Nam id varius mi, et sodales odio. Morbi ex nibh, pharetra aliquet dolor eu, mollis sodales nibh. Proin id consectetur nisl.</p>
  <div class="read-more"><i></i>Read More</div>
</article>
<article class="abs news-card" style="left:484px">
  <h3 class="news-head">Lorem ipsum dolor sit amet, consectetur adipiscing elit.</h3>
  <div class="news-meta">by Tobias Greene, on June 22</div>
  <p class="news-copy">Nam id varius mi, et sodales odio. Morbi ex nibh, pharetra aliquet dolor eu, mollis sodales nibh. Proin id consectetur nisl.</p>
  <div class="read-more"><i></i>Read More</div>
</article>
<article class="abs news-card" style="left:734px">
  <h3 class="news-head">Lorem ipsum dolor sit amet, consectetur adipiscing elit.</h3>
  <div class="news-meta">by Tobias Greene, on June 22</div>
  <p class="news-copy">Nam id varius mi, et sodales odio. Morbi ex nibh, pharetra aliquet dolor eu, mollis sodales nibh. Proin id consectetur nisl.</p>
  <div class="read-more"><i></i>Read More</div>
</article>

<!-- contact -->
<div class="abs contact-art" role="img" aria-label="Illustration of a customer support agent with a headset at a computer, surrounded by chat bubbles"></div>
<h2 class="abs contact-title">Contact us today,<br>We are here to help you</h2>
<p class="abs contact-copy">Lorem ipsum dolor sit amet, consectetur adipiscing elit. Duis libero sapien, sodales a scelerisque eget, aliquet at arcu.</p>
<div class="abs field" style="left:578px;top:2944px;width:189px;height:34px">First name</div>
<div class="abs field" style="left:776px;top:2944px;width:190px;height:34px">Last name</div>
<div class="abs field" style="left:578px;top:2989px;width:189px;height:34px">Email address</div>
<div class="abs field" style="left:776px;top:2989px;width:190px;height:34px">Phone</div>
<div class="abs field" style="left:578px;top:3033px;width:388px;height:77px">Your comments</div>
<a class="abs btn submit-btn">Submit Now</a>

<!-- footer -->
<div class="abs footer-bg"></div>
<div class="abs foot-brand">
  <div class="brand-dot"></div>
  <div class="foot-name">ledgerwise reach</div>
  <div class="foot-tag">The Demand Generation Company</div>
</div>
<p class="abs foot-copy">Ledgerwise Reach can deliver high quality sales leads from any country in the world. This can include leads via email or telemarketing, account-based targeting (ABM) or identifying need and pain points through BANT / SQL campaigns.</p>
<div class="abs foot-col" style="left:555px;top:3357px">
  <h4>PAGES</h4>
  <ul><li>Home</li><li>About Us</li><li>Our Services</li><li>Prospora &amp; QA</li><li>Technology</li><li>Intent Data</li><li>Testimonials</li><li>Contact Us</li></ul>
</div>
<div class="abs foot-col" style="left:680px;top:3357px">
  <h4>RESORCE</h4>
  <ul><li>FAQ</li><li>Terms &amp; Conditions</li><li>Privacy Policy</li><li>Sitemap</li></ul>
</div>
<div class="abs foot-col foot-contact" style="left:828px;top:3357px">
  <h4>CONTACT</h4>
  <ul>
    <li><svg width="10" height="13" viewBox="0 0 10 13"><path d="M5 0a5 5 0 015 5c0 3.5-5 8-5 8S0 8.5 0 5a5 5 0 015-5z" fill="var(--red)"/><circle cx="5" cy="5" r="1.8" fill="#fff"/></svg><span>Alder Quay Road<br>48 London, England<br>SE9 4QX, GB</span></li>
    <li><svg width="10" height="10" viewBox="0 0 24 24"><path fill="var(--red)" d="M6.6 10.8a15 15 0 006.6 6.6l2.2-2.2a1 1 0 011-.25 11.4 11.4 0 003.6.6 1 1 0 011 1V20a1 1 0 01-1 1A17 17 0 013 4a1 1 0 011-1h3.5a1 1 0 011 1c0 1.25.2 2.45.57 3.57a1 1 0 01-.25 1z"/></svg><span>(020) 555-0148</span></li>
    <li><svg width="11" height="9" viewBox="0 0 16 12"><rect width="16" height="12" rx="1.5" fill="var(--red)"/><path d="M1 1l7 5 7-5" stroke="#fff" stroke-width="1.4" fill="none"/></svg><span>info@ledgerwisereach.example</span></li>
  </ul>
</div>
<div class="abs copyright">© 2020 ledgerwisereach. All Rights Reserved.</div>
<div class="abs social"><span role="img" aria-label="Social profile link"></span><span role="img" aria-label="Professional network profile link"></span></div>

</body>
</html>
```